Letterhead Design for Law Firm that Specializes in Property Damage Litigation

We are looking for a redesign of our letterhead. Our current letterhead lists all of our current staff members and we'd like to come up with a design that does NOT list all of the staff members so that it does not need to be updated with every newly hired employee. Must be in editable format.

We are a law firm that specializes in property damage, so we need something that is professional, yet modern. The final design should use our existing logo and should use a blue color scheme (alternate colors would be gray, black, and white).

Industry/Entity Type

Legal

Colors
0054AA
0677BA
7BADD7
CADEEF
E8F1F8

```html
<!DOCTYPE html>
<html lang="en">
<head>
<meta charset="utf-8">
<title>Harlow Bennett &amp; Crane Letterhead</title>
<link href="https://fonts.googleapis.com/css2?family=PT+Serif:wght@400;700&family=Open+Sans:wght@400;600&display=swap" rel="stylesheet">
<style>
  :root {
    --backdrop: #dcdcdc;
    --paper: #ffffff;
    --navy: #1f3a6b;
    --gray-line: #555a60;
    --gray-text: #5f6368;
    --rule-light: #7f8c9f;
  }
  * { margin: 0; padding: 0; box-sizing: border-box; }
  html, body {
    width: 1200px; height: 960px; overflow: hidden;
    background: var(--backdrop);
  }
  .letterhead {
    position: absolute; left: 260px; top: 40px;
    width: 680px; height: 880px;
    background: var(--paper);
    box-shadow: 0 6px 24px rgba(0,0,0,0.12);
    font-family: "PT Serif", Georgia, serif;
  }
  .frame-lines { position: absolute; inset: 0; width: 680px; height: 880px; }
  .office { position: absolute; top: 38px; font-size: 12.5px; line-height: 1.35; }
  .office h2 { font-size: 13px; font-weight: 700; letter-spacing: 0.03em; margin-bottom: 8px; }
  .office p { margin-bottom: 4px; }
  .office .address { margin-top: 6px; line-height: 1.15; }
  .office-primary { left: 40px; color: var(--gray-text); }
  .office-primary h2 { color: var(--gray-text); }
  .office-secondary { left: 245px; top: 26px; color: var(--navy); }
  .firm-block { position: absolute; left: 460px; top: 20px; width: 195px; text-align: right; }
  .firm-name {
    font-family: "PT Serif", Georgia, serif; font-weight: 400;
    color: var(--navy); font-size: 17px; line-height: 1.02;
    text-transform: uppercase; letter-spacing: 0.04em;
  }
  .firm-tagline {
    font-family: "Open Sans", Arial, sans-serif; font-size: 6.6px;
    letter-spacing: 0.16em; color: var(--gray-text);
    text-transform: uppercase; margin-top: 7px; margin-left: 30px;
    padding-bottom: 5px; border-bottom: 1px solid var(--rule-light);
    white-space: nowrap;
  }
  .firm-contact {
    font-family: "Open Sans", Arial, sans-serif; font-size: 9px;
    color: #333; margin-top: 6px; white-space: nowrap;
  }
</style>
</head>
<body>
  <main class="letterhead">
    <svg class="frame-lines" viewBox="0 0 680 880" aria-hidden="true">
      <polyline points="60,160 420,160 470,0" fill="none" stroke="var(--gray-line)" stroke-width="3"/>
      <polyline points="655,128 440,128 480,0" fill="none" stroke="var(--navy)" stroke-width="3"/>
      <line x1="612" y1="880" x2="657" y2="745" stroke="var(--gray-line)" stroke-width="3"/>
      <line x1="628" y1="880" x2="673" y2="745" stroke="var(--navy)" stroke-width="3"/>
    </svg>

    <section class="office office-primary">
      <h2>RIVERTON OFFICE</h2>
      <p>555.010.3300</p>
      <p>555.010.7650</p>
      <p class="address">1200 Market Row<br>Suite 840<br>Riverton, ST 10400</p>
    </section>

    <section class="office office-secondary">
      <h2>LAKEWOOD OFFICE</h2>
      <p>555.010.6120</p>
      <p>555.010.7650</p>
      <p class="address">400 Orchard Lane North<br>Suite 310<br>Lakewood, ST 20500</p>
    </section>

    <header class="firm-block">
      <div class="firm-name">Harlow<br>Bennett &amp;<br>Crane</div>
      <div class="firm-tagline">Property Loss Trial Counsel</div>
      <div class="firm-contact">www.hbclegal.example | (555) 010-4400</div>
    </header>
  </main>
</body>
</html>
```